Piano genealogy graphs template, for a large poster printing

Hello and thank you for your interest in my project.
I need a poster template, so I can create structures similar to the one I have uploaded. I want to completely replace or improve my poor previous design which is attached.
I need to be able to input names and dates into boxes of various colors, arrows pointing between boxes. I would also like to be able to label each graph (not each box).
I am looking at something that would be legible when printed, in a one consistent professional layout of 2A0 (around 1189x1682 mm) poster (I know it is large). The design template required here can include just few sample text boxes with sample flags on a suitable background, for me to multiply later and spread across the whole poster.
The positioning of the boxes is not important.
Please let me know if more clarification is required.
Thank you for your help.

Feel free to follow what I have attached in the file, or change the design completely.

UPDATE 4/12: I have uploaded two more graphs as an example. At this stage of the contest, I would like to have one of those graphs done, and I am planning to offer a 'freelance job' to one or two designers, who will be willing to do the whole 10 graphs on one poster.
Updates

Reason: Dear Designers, Since the project is rather complex and large-scale, I have decided to give everyone more time to work on their designs. I will consider extending it further if any of you require additional time. Best wishes, bronisław

Dear Designers, I would like to inform you that the contest for my poster is now closed and that I have assigned the prizes. I would like to thank all of you for submiting your high-quality designs, and for your participation. It was a great pleasure working with all of you. Due to the large size of the project itself (large number of graphs to be fitted on a single poster), I had to focus on providing feedback to only those designers who provided projects closest to what I was expecting at the early stages of the contest. I wish you all the best for the future, Kind regards, Bronisław

Target Market(s)

Pianists, historians

Industry/Entity Type

Printing

Requirements
Must have
• Consistent design, but allow to clearly delineate various genealogy trees.

```html
<!DOCTYPE html>
<html lang="en">
<head>
<meta charset="utf-8">
<title>Genealogical Trees of Pianists</title>
<link rel="stylesheet" href="https://fonts.googleapis.com/css2?family=Fira+Sans:wght@400;600&display=swap">
<style>
  :root{
    --bg:#023a4f;
    --title:#1ec9c9;
    --node:#5ad67d;
    --node-head:#00cccc;
    --node-border:#a9f1ef;
    --name-ink:#0d3a44;
    --list-ink:#2a5a52;
    --link:#16b3e6;
    --arrow:#5ad67d;
    --flag-blue:#1f2fe0;
    --flag-white:#ffffff;
    --flag-red:#f01c24;
    --flag-edge:#0d2a3a;
  }
  *{box-sizing:border-box;margin:0;padding:0}
  html,body{width:960px;height:1200px;overflow:hidden;background:var(--bg)}
  body{font-family:"Fira Sans",sans-serif}
  .poster{position:relative;width:1200px;height:1500px;transform:scale(.8);transform-origin:0 0;background:var(--bg)}
  .poster-title{position:absolute;top:22px;left:0;width:100%;text-align:center;font-weight:600;font-size:38px;color:var(--title);letter-spacing:.2px}
  .links{position:absolute;inset:0}
  .links path{fill:none;stroke:var(--link);stroke-width:3.5;stroke-dasharray:8 6}
  .links polygon{fill:var(--arrow)}
  .tree-node{position:absolute;background:var(--node);border:3px solid var(--node-border);border-radius:16px;overflow:hidden}
  .node-head{position:relative;height:54px;background:var(--node-head);border-bottom:3px solid var(--node-border);padding:7px 10px 0 30px}
  .node-name{font-size:15px;font-weight:600;line-height:19px;color:var(--name-ink);text-align:center}
  .flag{display:block;width:24px;height:15px}
  .node-head .flag{position:absolute;left:16px;top:14px;width:26px;height:16px}
  .student-list{list-style:none;padding:16px 18px 0 10px}
  .student-list.is-long{padding-left:18px}
  .student-list li{display:flex;justify-content:space-between;align-items:center;font-size:13px;line-height:16.9px;height:16.9px;color:var(--list-ink)}
  .is-single{padding:8px 10px 0 30px}
  .is-single .flag{position:absolute;left:18px;top:17px;width:26px;height:16px}
</style>
</head>
<body>
<main class="poster">
  <h1 class="poster-title">Genealogical Trees of Pianists</h1>

  <svg class="links" viewBox="0 0 1200 1500" width="1200" height="1500" aria-hidden="true">
    <path d="M582 1412V1360"/>
    <path d="M582 1280V1250"/>
    <path d="M582 1244V1216M286 1184V1206Q286 1216 296 1216H898Q908 1216 908 1206V1184M582 1216V1172"/>
    <path d="M582 921V868"/>
    <path d="M430 1052H272Q262 1052 262 1042V1012M770 1052H928Q938 1052 938 1042V1012"/>
    <path d="M430 832H260Q250 832 250 822V802M770 749H945Q955 749 955 739V709"/>
    <path d="M582 612V540"/>
    <path d="M582 534V330Q582 320 592 320H678Q688 320 688 310V288"/>
    <path d="M194 494V515Q194 525 204 525H976Q986 525 986 515V494M476 525V422M715 525V491"/>
    <path d="M489 344V288M489 316H204Q194 316 194 306V288"/>
    <path d="M720 344V326Q720 316 730 316H942Q952 316 952 306V288"/>
    <path d="M1006 344V288"/>
    <polygon points="577,1364 582,1355 587,1364"/>
    <polygon points="577,1245 582,1236 587,1245"/>
    <polygon points="577,1176 582,1167 587,1176"/>
    <polygon points="281,1184 286,1175 291,1184"/>
    <polygon points="903,1184 908,1175 913,1184"/>
    <polygon points="577,868 582,859 587,868"/>
    <polygon points="257,1014 262,1005 267,1014"/>
    <polygon points="933,1014 938,1005 943,1014"/>
    <polygon points="245,804 250,795 255,804"/>
    <polygon points="950,711 955,702 960,711"/>
    <polygon points="577,543 582,534 587,543"/>
    <polygon points="189,496 194,487 199,496"/>
    <polygon points="471,424 476,415 481,424"/>
    <polygon points="710,493 715,484 720,493"/>
    <polygon points="981,496 986,487 991,496"/>
    <polygon points="683,289 688,280 693,289"/>
    <polygon points="484,289 489,280 494,289"/>
    <polygon points="189,289 194,280 199,289"/>
    <polygon points="947,289 952,280 957,289"/>
    <polygon points="1001,289 1006,280 1011,289"/>
  </svg>

  <!-- Row 1 -->
  <article class="tree-node" style="left:73px;top:136px;width:243px;height:138px">
    <header class="node-head"><svg class="flag" viewBox="0 0 30 20"><rect width="10" height="20" fill="var(--flag-blue)"/><rect x="10" width="10" height="20" fill="var(--flag-white)"/><rect x="20" width="10" height="20" fill="var(--flag-red)"/><rect x=".5" y=".5" width="29" height="19" fill="none" stroke="var(--flag-edge)"/></svg><h2 class="node-name">Henri Valmont<br>(1916-2008) Students:</h2></header>
    <ul class="student-list">
      <li>Jean-Luc Marchand (1947)<svg class="flag" viewBox="0 0 30 20"><rect width="10" height="20" fill="var(--flag-blue)"/><rect x="10" width="10" height="20" fill="var(--flag-white)"/><rect x="20" width="10" height="20" fill="var(--flag-red)"/><rect x=".5" y=".5" width="29" height="19" fill="none" stroke="var(--flag-edge)"/></svg></li>
      <li>Jacques Dorval (1947)<svg class="flag" viewBox="0 0 30 20"><rect width="10" height="20" fill="var(--flag-blue)"/><rect x="10" width="10" height="20" fill="var(--flag-white)"/><rect x="20" width="10" height="20" fill="var(--flag-red)"/><rect x=".5" y=".5" width="29" height="19" fill="none" stroke="var(--flag-edge)"/></svg></li>
      <li>Jean-Paul Fontaine (1944)<svg class="flag" viewBox="0 0 30 20"><rect width="10" height="20" fill="var(--flag-blue)"/><rect x="10" width="10" height="20" fill="var(--flag-white)"/><rect x="20" width="10" height="20" fill="var(--flag-red)"/><rect x=".5" y=".5" width="29" height="19" fill="none" stroke="var(--flag-edge)"/></svg></li>
    </ul>
  </article>
  <article class="tree-node" style="left:344px;top:136px;width:242px;height:138px">
    <header class="node-head"><svg class="flag" viewBox="0 0 30 20"><rect width="10" height="20" fill="var(--flag-blue)"/><rect x="10" width="10" height="20" fill="var(--flag-white)"/><rect x="20" width="10" height="20" fill="var(--flag-red)"/><rect x=".5" y=".5" width="29" height="19" fill="none" stroke="var(--flag-edge)"/></svg><h2 class="node-name">Henri Valmont<br>(1916-2008) Students:</h2></header>
    <ul class="student-list">
      <li>Jean-Luc Marchand (1947)<svg class="flag" viewBox="0 0 30 20"><rect width="10" height="20" fill="var(--flag-blue)"/><rect x="10" width="10" height="20" fill="var(--flag-white)"/><rect x="20" width="10" height="20" fill="var(--flag-red)"/><rect x=".5" y=".5" width="29" height="19" fill="none" stroke="var(--flag-edge)"/></svg></li>
      <li>Jacques Dorval (1947)<svg class="flag" viewBox="0 0 30 20"><rect width="10" height="20" fill="var(--flag-blue)"/><rect x="10" width="10" height="20" fill="var(--flag-white)"/><rect x="20" width="10" height="20" fill="var(--flag-red)"/><rect x=".5" y=".5" width="29" height="19" fill="none" stroke="var(--flag-edge)"/></svg></li>
      <li>Jean-Paul Fontaine (1944)<svg class="flag" viewBox="0 0 30 20"><rect width="10" height="20" fill="var(--flag-blue)"/><rect x="10" width="10" height="20" fill="var(--flag-white)"/><rect x="20" width="10" height="20" fill="var(--flag-red)"/><rect x=".5" y=".5" width="29" height="19" fill="none" stroke="var(--flag-edge)"/></svg></li>
    </ul>
  </article>
  <article class="tree-node" style="left:614px;top:136px;width:243px;height:138px">
    <header class="node-head"><svg class="flag" viewBox="0 0 30 20"><rect width="10" height="20" fill="var(--flag-blue)"/><rect x="10" width="10" height="20" fill="var(--flag-white)"/><rect x="20" width="10" height="20" fill="var(--flag-red)"/><rect x=".5" y=".5" width="29" height="19" fill="none" stroke="var(--flag-edge)"/></svg><h2 class="node-name">Henri Valmont<br>(1916-2008) Students:</h2></header>
    <ul class="student-list">
      <li>Jean-Luc Marchand (1947)<svg class="flag" viewBox="0 0 30 20"><rect width="10" height="20" fill="var(--flag-blue)"/><rect x="10" width="10" height="20" fill="var(--flag-white)"/><rect x="20" width="10" height="20" fill="var(--flag-red)"/><rect x=".5" y=".5" width="29" height="19" fill="none" stroke="var(--flag-edge)"/></svg></li>
      <li>Jacques Dorval (1947)<svg class="flag" viewBox="0 0 30 20"><rect width="10" height="20" fill="var(--flag-blue)"/><rect x="10" width="10" height="20" fill="var(--flag-white)"/><rect x="20" width="10" height="20" fill="var(--flag-red)"/><rect x=".5" y=".5" width="29" height="19" fill="none" stroke="var(--flag-edge)"/></svg></li>
      <li>Jean-Paul Fontaine (1944)<svg class="flag" viewBox="0 0 30 20"><rect width="10" height="20" fill="var(--flag-blue)"/><rect x="10" width="10" height="20" fill="var(--flag-white)"/><rect x="20" width="10" height="20" fill="var(--flag-red)"/><rect x=".5" y=".5" width="29" height="19" fill="none" stroke="var(--flag-edge)"/></svg></li>
    </ul>
  </article>
  <article class="tree-node" style="left:885px;top:136px;width:243px;height:138px">
    <header class="node-head"><svg class="flag" viewBox="0 0 30 20"><rect width="10" height="20" fill="var(--flag-blue)"/><rect x="10" width="10" height="20" fill="var(--flag-white)"/><rect x="20" width="10" height="20" fill="var(--flag-red)"/><rect x=".5" y=".5" width="29" height="19" fill="none" stroke="var(--flag-edge)"/></svg><h2 class="node-name">Henri Valmont<br>(1916-2008) Students:</h2></header>
    <ul class="student-list">
      <li>Jean-Luc Marchand (1947)<svg class="flag" viewBox="0 0 30 20"><rect width="10" height="20" fill="var(--flag-blue)"/><rect x="10" width="10" height="20" fill="var(--flag-white)"/><rect x="20" width="10" height="20" fill="var(--flag-red)"/><rect x=".5" y=".5" width="29" height="19" fill="none" stroke="var(--flag-edge)"/></svg></li>
      <li>Jacques Dorval (1947)<svg class="flag" viewBox="0 0 30 20"><rect width="10" height="20" fill="var(--flag-blue)"/><rect x="10" width="10" height="20" fill="var(--flag-white)"/><rect x="20" width="10" height="20" fill="var(--flag-red)"/><rect x=".5" y=".5" width="29" height="19" fill="none" stroke="var(--flag-edge)"/></svg></li>
      <li>Jean-Paul Fontaine (1944)<svg class="flag" viewBox="0 0 30 20"><rect width="10" height="20" fill="var(--flag-blue)"/><rect x="10" width="10" height="20" fill="var(--flag-white)"/><rect x="20" width="10" height="20" fill="var(--flag-red)"/><rect x=".5" y=".5" width="29" height="19" fill="none" stroke="var(--flag-edge)"/></svg></li>
    </ul>
  </article>

  <!-- Row 2 -->
  <article class="tree-node" style="left:93px;top:344px;width:283px;height:138px">
    <header class="node-head"><svg class="flag" viewBox="0 0 30 20"><rect width="10" height="20" fill="var(--flag-blue)"/><rect x="10" width="10" height="20" fill="var(--flag-white)"/><rect x="20" width="10" height="20" fill="var(--flag-red)"/><rect x=".5" y=".5" width="29" height="19" fill="none" stroke="var(--flag-edge)"/></svg><h2 class="node-name">Henri Valmont<br>(1916-2008) Students:</h2></header>
    <ul class="student-list is-long">
      <li>Jean-Luc Marchand (1947)<svg class="flag" viewBox="0 0 30 20"><rect width="10" height="20" fill="var(--flag-blue)"/><rect x="10" width="10" height="20" fill="var(--flag-white)"/><rect x="20" width="10" height="20" fill="var(--flag-red)"/><rect x=".5" y=".5" width="29" height="19" fill="none" stroke="var(--flag-edge)"/></svg></li>
      <li>Jacques Dorval (1947)<svg class="flag" viewBox="0 0 30 20"><rect width="10" height="20" fill="var(--flag-blue)"/><rect x="10" width="10" height="20" fill="var(--flag-white)"/><rect x="20" width="10" height="20" fill="var(--flag-red)"/><rect x=".5" y=".5" width="29" height="19" fill="none" stroke="var(--flag-edge)"/></svg></li>
      <li>Jean-Paul Fontaine (1944)<svg class="flag" viewBox="0 0 30 20"><rect width="10" height="20" fill="var(--flag-blue)"/><rect x="10" width="10" height="20" fill="var(--flag-white)"/><rect x="20" width="10" height="20" fill="var(--flag-red)"/><rect x=".5" y=".5" width="29" height="19" fill="none" stroke="var(--flag-edge)"/></svg></li>
    </ul>
  </article>
  <article class="tree-node is-single" style="left:398px;top:344px;width:172px;height:66px">
    <svg class="flag" viewBox="0 0 30 20"><rect width="10" height="20" fill="var(--flag-blue)"/><rect x="10" width="10" height="20" fill="var(--flag-white)"/><rect x="20" width="10" height="20" fill="var(--flag-red)"/><rect x=".5" y=".5" width="29" height="19" fill="none" stroke="var(--flag-edge)"/></svg><h2 class="node-name">Henri Valmont<br>(1916-2008)</h2>
  </article>
  <article class="tree-node" style="left:595px;top:344px;width:242px;height:138px">
    <header class="node-head"><svg class="flag" viewBox="0 0 30 20"><rect width="10" height="20" fill="var(--flag-blue)"/><rect x="10" width="10" height="20" fill="var(--flag-white)"/><rect x="20" width="10" height="20" fill="var(--flag-red)"/><rect x=".5" y=".5" width="29" height="19" fill="none" stroke="var(--flag-edge)"/></svg><h2 class="node-name">Henri Valmont<br>(1916-2008) Students:</h2></header>
    <ul class="student-list">
      <li>Jean-Luc Marchand (1947)<svg class="flag" viewBox="0 0 30 20"><rect width="10" height="20" fill="var(--flag-blue)"/><rect x="10" width="10" height="20" fill="var(--flag-white)"/><rect x="20" width="10" height="20" fill="var(--flag-red)"/><rect x=".5" y=".5" width="29" height="19" fill="none" stroke="var(--flag-edge)"/></svg></li>
      <li>Jacques Dorval (1947)<svg class="flag" viewBox="0 0 30 20"><rect width="10" height="20" fill="var(--flag-blue)"/><rect x="10" width="10" height="20" fill="var(--flag-white)"/><rect x="20" width="10" height="20" fill="var(--flag-red)"/><rect x=".5" y=".5" width="29" height="19" fill="none" stroke="var(--flag-edge)"/></svg></li>
      <li>Jean-Paul Fontaine (1944)<svg class="flag" viewBox="0 0 30 20"><rect width="10" height="20" fill="var(--flag-blue)"/><rect x="10" width="10" height="20" fill="var(--flag-white)"/><rect x="20" width="10" height="20" fill="var(--flag-red)"/><rect x=".5" y=".5" width="29" height="19" fill="none" stroke="var(--flag-edge)"/></svg></li>
    </ul>
  </article>
  <article class="tree-node" style="left:865px;top:344px;width:243px;height:138px">
    <header class="node-head"><svg class="flag" viewBox="0 0 30 20"><rect width="10" height="20" fill="var(--flag-blue)"/><rect x="10" width="10" height="20" fill="var(--flag-white)"/><rect x="20" width="10" height="20" fill="var(--flag-red)"/><rect x=".5" y=".5" width="29" height="19" fill="none" stroke="var(--flag-edge)"/></svg><h2 class="node-name">Henri Valmont<br>(1916-2008) Students:</h2></header>
    <ul class="student-list">
      <li>Jean-Luc Marchand (1947)<svg class="flag" viewBox="0 0 30 20"><rect width="10" height="20" fill="var(--flag-blue)"/><rect x="10" width="10" height="20" fill="var(--flag-white)"/><rect x="20" width="10" height="20" fill="var(--flag-red)"/><rect x=".5" y=".5" width="29" height="19" fill="none" stroke="var(--flag-edge)"/></svg></li>
      <li>Jacques Dorval (1947)<svg class="flag" viewBox="0 0 30 20"><rect width="10" height="20" fill="var(--flag-blue)"/><rect x="10" width="10" height="20" fill="var(--flag-white)"/><rect x="20" width="10" height="20" fill="var(--flag-red)"/><rect x=".5" y=".5" width="29" height="19" fill="none" stroke="var(--flag-edge)"/></svg></li>
      <li>Jean-Paul Fontaine (1944)<svg class="flag" viewBox="0 0 30 20"><rect width="10" height="20" fill="var(--flag-blue)"/><rect x="10" width="10" height="20" fill="var(--flag-white)"/><rect x="20" width="10" height="20" fill="var(--flag-red)"/><rect x=".5" y=".5" width="29" height="19" fill="none" stroke="var(--flag-edge)"/></svg></li>
    </ul>
  </article>

  <!-- Row 3 -->
  <article class="tree-node" style="left:112px;top:552px;width:289px;height:241px">
    <header class="node-head"><svg class="flag" viewBox="0 0 30 20"><rect width="10" height="20" fill="var(--flag-blue)"/><rect x="10" width="10" height="20" fill="var(--flag-white)"/><rect x="20" width="10" height="20" fill="var(--flag-red)"/><rect x=".5" y=".5" width="29" height="19" fill="none" stroke="var(--flag-edge)"/></svg><h2 class="node-name">Henri Valmont<br>(1916-2008) Students:</h2></header>
    <ul class="student-list is-long">
      <li>Jean-Luc Marchand (1947)<svg class="flag" viewBox="0 0 30 20"><rect width="10" height="20" fill="var(--flag-blue)"/><rect x="10" width="10" height="20" fill="var(--flag-white)"/><rect x="20" width="10" height="20" fill="var(--flag-red)"/><rect x=".5" y=".5" width="29" height="19" fill="none" stroke="var(--flag-edge)"/></svg></li>
      <li>Jacques Dorval (1947)<svg class="flag" viewBox="0 0 30 20"><rect width="10" height="20" fill="var(--flag-blue)"/><rect x="10" width="10" height="20" fill="var(--flag-white)"/><rect x="20" width="10" height="20" fill="var(--flag-red)"/><rect x=".5" y=".5" width="29" height="19" fill="none" stroke="var(--flag-edge)"/></svg></li>
      <li>Jean-Paul Fontaine (1944)<svg class="flag" viewBox="0 0 30 20"><rect width="10" height="20" fill="var(--flag-blue)"/><rect x="10" width="10" height="20" fill="var(--flag-white)"/><rect x="20" width="10" height="20" fill="var(--flag-red)"/><rect x=".5" y=".5" width="29" height="19" fill="none" stroke="var(--flag-edge)"/></svg></li>
      <li>Jean-Luc Marchand (1947)<svg class="flag" viewBox="0 0 30 20"><rect width="10" height="20" fill="var(--flag-blue)"/><rect x="10" width="10" height="20" fill="var(--flag-white)"/><rect x="20" width="10" height="20" fill="var(--flag-red)"/><rect x=".5" y=".5" width="29" height="19" fill="none" stroke="var(--flag-edge)"/></svg></li>
      <li>Jacques Dorval (1947)<svg class="flag" viewBox="0 0 30 20"><rect width="10" height="20" fill="var(--flag-blue)"/><rect x="10" width="10" height="20" fill="var(--flag-white)"/><rect x="20" width="10" height="20" fill="var(--flag-red)"/><rect x=".5" y=".5" width="29" height="19" fill="none" stroke="var(--flag-edge)"/></svg></li>
      <li>Jean-Paul Fontaine (1944)<svg class="flag" viewBox="0 0 30 20"><rect width="10" height="20" fill="var(--flag-blue)"/><rect x="10" width="10" height="20" fill="var(--flag-white)"/><rect x="20" width="10" height="20" fill="var(--flag-red)"/><rect x=".5" y=".5" width="29" height="19" fill="none" stroke="var(--flag-edge)"/></svg></li>
      <li>Jean-Luc Marchand (1947)<svg class="flag" viewBox="0 0 30 20"><rect width="10" height="20" fill="var(--flag-blue)"/><rect x="10" width="10" height="20" fill="var(--flag-white)"/><rect x="20" width="10" height="20" fill="var(--flag-red)"/><rect x=".5" y=".5" width="29" height="19" fill="none" stroke="var(--flag-edge)"/></svg></li>
      <li>Jacques Dorval (1947)<svg class="flag" viewBox="0 0 30 20"><rect width="10" height="20" fill="var(--flag-blue)"/><rect x="10" width="10" height="20" fill="var(--flag-white)"/><rect x="20" width="10" height="20" fill="var(--flag-red)"/><rect x=".5" y=".5" width="29" height="19" fill="none" stroke="var(--flag-edge)"/></svg></li>
      <li>Jean-Paul Fontaine (1944)</li>
    </ul>
  </article>
  <article class="tree-node" style="left:430px;top:612px;width:341px;height:242px">
    <header class="node-head"><svg class="flag" viewBox="0 0 30 20"><rect width="10" height="20" fill="var(--flag-blue)"/><rect x="10" width="10" height="20" fill="var(--flag-white)"/><rect x="20" width="10" height="20" fill="var(--flag-red)"/><rect x=".5" y=".5" width="29" height="19" fill="none" stroke="var(--flag-edge)"/></svg><h2 class="node-name">Henri Valmont<br>(1916-2008) Students:</h2></header>
    <ul class="student-list is-long">
      <li>Jean-Luc Marchand (1947)<svg class="flag" viewBox="0 0 30 20"><rect width="10" height="20" fill="var(--flag-blue)"/><rect x="10" width="10" height="20" fill="var(--flag-white)"/><rect x="20" width="10" height="20" fill="var(--flag-red)"/><rect x=".5" y=".5" width="29" height="19" fill="none" stroke="var(--flag-edge)"/></svg></li>
      <li>Jacques Dorval (1947)<svg class="flag" viewBox="0 0 30 20"><rect width="10" height="20" fill="var(--flag-blue)"/><rect x="10" width="10" height="20" fill="var(--flag-white)"/><rect x="20" width="10" height="20" fill="var(--flag-red)"/><rect x=".5" y=".5" width="29" height="19" fill="none" stroke="var(--flag-edge)"/></svg></li>
      <li>Jean-Paul Fontaine (1944)<svg class="flag" viewBox="0 0 30 20"><rect width="10" height="20" fill="var(--flag-blue)"/><rect x="10" width="10" height="20" fill="var(--flag-white)"/><rect x="20" width="10" height="20" fill="var(--flag-red)"/><rect x=".5" y=".5" width="29" height="19" fill="none" stroke="var(--flag-edge)"/></svg></li>
      <li>Jean-Luc Marchand (1947)<svg class="flag" viewBox="0 0 30 20"><rect width="10" height="20" fill="var(--flag-blue)"/><rect x="10" width="10" height="20" fill="var(--flag-white)"/><rect x="20" width="10" height="20" fill="var(--flag-red)"/><rect x=".5" y=".5" width="29" height="19" fill="none" stroke="var(--flag-edge)"/></svg></li>
      <li>Jacques Dorval (1947)<svg class="flag" viewBox="0 0 30 20"><rect width="10" height="20" fill="var(--flag-blue)"/><rect x="10" width="10" height="20" fill="var(--flag-white)"/><rect x="20" width="10" height="20" fill="var(--flag-red)"/><rect x=".5" y=".5" width="29" height="19" fill="none" stroke="var(--flag-edge)"/></svg></li>
      <li>Jean-Paul Fontaine (1944)<svg class="flag" viewBox="0 0 30 20"><rect width="10" height="20" fill="var(--flag-blue)"/><rect x="10" width="10" height="20" fill="var(--flag-white)"/><rect x="20" width="10" height="20" fill="var(--flag-red)"/><rect x=".5" y=".5" width="29" height="19" fill="none" stroke="var(--flag-edge)"/></svg></li>
      <li>Jean-Luc Marchand (1947)<svg class="flag" viewBox="0 0 30 20"><rect width="10" height="20" fill="var(--flag-blue)"/><rect x="10" width="10" height="20" fill="var(--flag-white)"/><rect x="20" width="10" height="20" fill="var(--flag-red)"/><rect x=".5" y=".5" width="29" height="19" fill="none" stroke="var(--flag-edge)"/></svg></li>
      <li>Jacques Dorval (1947)<svg class="flag" viewBox="0 0 30 20"><rect width="10" height="20" fill="var(--flag-blue)"/><rect x="10" width="10" height="20" fill="var(--flag-white)"/><rect x="20" width="10" height="20" fill="var(--flag-red)"/><rect x=".5" y=".5" width="29" height="19" fill="none" stroke="var(--flag-edge)"/></svg></li>
      <li>Jean-Paul Fontaine (1944)<svg class="flag" viewBox="0 0 30 20"><rect width="10" height="20" fill="var(--flag-blue)"/><rect x="10" width="10" height="20" fill="var(--flag-white)"/><rect x="20" width="10" height="20" fill="var(--flag-red)"/><rect x=".5" y=".5" width="29" height="19" fill="none" stroke="var(--flag-edge)"/></svg></li>
    </ul>
  </article>
  <article class="tree-node" style="left:805px;top:555px;width:282px;height:137px">
    <header class="node-head"><svg class="flag" viewBox="0 0 30 20"><rect width="10" height="20" fill="var(--flag-blue)"/><rect x="10" width="10" height="20" fill="var(--flag-white)"/><rect x="20" width="10" height="20" fill="var(--flag-red)"/><rect x=".5" y=".5" width="29" height="19" fill="none" stroke="var(--flag-edge)"/></svg><h2 class="node-name">Henri Valmont<br>(1916-2008) Students:</h2></header>
    <ul class="student-list is-long">
      <li>Jean-Luc Marchand (1947)<svg class="flag" viewBox="0 0 30 20"><rect width="10" height="20" fill="var(--flag-blue)"/><rect x="10" width="10" height="20" fill="var(--flag-white)"/><rect x="20" width="10" height="20" fill="var(--flag-red)"/><rect x=".5" y=".5" width="29" height="19" fill="none" stroke="var(--flag-edge)"/></svg></li>
      <li>Jacques Dorval (1947)<svg class="flag" viewBox="0 0 30 20"><rect width="10" height="20" fill="var(--flag-blue)"/><rect x="10" width="10" height="20" fill="var(--flag-white)"/><rect x="20" width="10" height="20" fill="var(--flag-red)"/><rect x=".5" y=".5" width="29" height="19" fill="none" stroke="var(--flag-edge)"/></svg></li>
      <li>Jean-Paul Fontaine (1944)<svg class="flag" viewBox="0 0 30 20"><rect width="10" height="20" fill="var(--flag-blue)"/><rect x="10" width="10" height="20" fill="var(--flag-white)"/><rect x="20" width="10" height="20" fill="var(--flag-red)"/><rect x=".5" y=".5" width="29" height="19" fill="none" stroke="var(--flag-edge)"/></svg></li>
    </ul>
  </article>

  <!-- Row 4 -->
  <article class="tree-node" style="left:133px;top:861px;width:257px;height:138px">
    <header class="node-head"><svg class="flag" viewBox="0 0 30 20"><rect width="10" height="20" fill="var(--flag-blue)"/><rect x="10" width="10" height="20" fill="var(--flag-white)"/><rect x="20" width="10" height="20" fill="var(--flag-red)"/><rect x=".5" y=".5" width="29" height="19" fill="none" stroke="var(--flag-edge)"/></svg><h2 class="node-name">Henri Valmont<br>(1916-2008) Students:</h2></header>
    <ul class="student-list is-long">
      <li>Jean-Luc Marchand (1947)<svg class="flag" viewBox="0 0 30 20"><rect width="10" height="20" fill="var(--flag-blue)"/><rect x="10" width="10" height="20" fill="var(--flag-white)"/><rect x="20" width="10" height="20" fill="var(--flag-red)"/><rect x=".5" y=".5" width="29" height="19" fill="none" stroke="var(--flag-edge)"/></svg></li>
      <li>Jacques Dorval (1947)<svg class="flag" viewBox="0 0 30 20"><rect width="10" height="20" fill="var(--flag-blue)"/><rect x="10" width="10" height="20" fill="var(--flag-white)"/><rect x="20" width="10" height="20" fill="var(--flag-red)"/><rect x=".5" y=".5" width="29" height="19" fill="none" stroke="var(--flag-edge)"/></svg></li>
      <li>Jean-Paul Fontaine (1944)<svg class="flag" viewBox="0 0 30 20"><rect width="10" height="20" fill="var(--flag-blue)"/><rect x="10" width="10" height="20" fill="var(--flag-white)"/><rect x="20" width="10" height="20" fill="var(--flag-red)"/><rect x=".5" y=".5" width="29" height="19" fill="none" stroke="var(--flag-edge)"/></svg></li>
    </ul>
  </article>
  <article class="tree-node" style="left:430px;top:921px;width:341px;height:242px">
    <header class="node-head"><svg class="flag" viewBox="0 0 30 20"><rect width="10" height="20" fill="var(--flag-blue)"/><rect x="10" width="10" height="20" fill="var(--flag-white)"/><rect x="20" width="10" height="20" fill="var(--flag-red)"/><rect x=".5" y=".5" width="29" height="19" fill="none" stroke="var(--flag-edge)"/></svg><h2 class="node-name">Henri Valmont<br>(1916-2008) Students:</h2></header>
    <ul class="student-list is-long">
      <li>Jean-Luc Marchand (1947)<svg class="flag" viewBox="0 0 30 20"><rect width="10" height="20" fill="var(--flag-blue)"/><rect x="10" width="10" height="20" fill="var(--flag-white)"/><rect x="20" width="10" height="20" fill="var(--flag-red)"/><rect x=".5" y=".5" width="29" height="19" fill="none" stroke="var(--flag-edge)"/></svg></li>
      <li>Jacques Dorval (1947)<svg class="flag" viewBox="0 0 30 20"><rect width="10" height="20" fill="var(--flag-blue)"/><rect x="10" width="10" height="20" fill="var(--flag-white)"/><rect x="20" width="10" height="20" fill="var(--flag-red)"/><rect x=".5" y=".5" width="29" height="19" fill="none" stroke="var(--flag-edge)"/></svg></li>
      <li>Jean-Paul Fontaine (1944)<svg class="flag" viewBox="0 0 30 20"><rect width="10" height="20" fill="var(--flag-blue)"/><rect x="10" width="10" height="20" fill="var(--flag-white)"/><rect x="20" width="10" height="20" fill="var(--flag-red)"/><rect x=".5" y=".5" width="29" height="19" fill="none" stroke="var(--flag-edge)"/></svg></li>
      <li>Jean-Luc Marchand (1947)<svg class="flag" viewBox="0 0 30 20"><rect width="10" height="20" fill="var(--flag-blue)"/><rect x="10" width="10" height="20" fill="var(--flag-white)"/><rect x="20" width="10" height="20" fill="var(--flag-red)"/><rect x=".5" y=".5" width="29" height="19" fill="none" stroke="var(--flag-edge)"/></svg></li>
      <li>Jacques Dorval (1947)<svg class="flag" viewBox="0 0 30 20"><rect width="10" height="20" fill="var(--flag-blue)"/><rect x="10" width="10" height="20" fill="var(--flag-white)"/><rect x="20" width="10" height="20" fill="var(--flag-red)"/><rect x=".5" y=".5" width="29" height="19" fill="none" stroke="var(--flag-edge)"/></svg></li>
      <li>Jean-Paul Fontaine (1944)<svg class="flag" viewBox="0 0 30 20"><rect width="10" height="20" fill="var(--flag-blue)"/><rect x="10" width="10" height="20" fill="var(--flag-white)"/><rect x="20" width="10" height="20" fill="var(--flag-red)"/><rect x=".5" y=".5" width="29" height="19" fill="none" stroke="var(--flag-edge)"/></svg></li>
      <li>Jean-Luc Marchand (1947)<svg class="flag" viewBox="0 0 30 20"><rect width="10" height="20" fill="var(--flag-blue)"/><rect x="10" width="10" height="20" fill="var(--flag-white)"/><rect x="20" width="10" height="20" fill="var(--flag-red)"/><rect x=".5" y=".5" width="29" height="19" fill="none" stroke="var(--flag-edge)"/></svg></li>
      <li>Jacques Dorval (1947)<svg class="flag" viewBox="0 0 30 20"><rect width="10" height="20" fill="var(--flag-blue)"/><rect x="10" width="10" height="20" fill="var(--flag-white)"/><rect x="20" width="10" height="20" fill="var(--flag-red)"/><rect x=".5" y=".5" width="29" height="19" fill="none" stroke="var(--flag-edge)"/></svg></li>
      <li>Jean-Paul Fontaine (1944)<svg class="flag" viewBox="0 0 30 20"><rect width="10" height="20" fill="var(--flag-blue)"/><rect x="10" width="10" height="20" fill="var(--flag-white)"/><rect x="20" width="10" height="20" fill="var(--flag-red)"/><rect x=".5" y=".5" width="29" height="19" fill="none" stroke="var(--flag-edge)"/></svg></li>
    </ul>
  </article>
  <article class="tree-node" style="left:811px;top:861px;width:257px;height:138px">
    <header class="node-head"><svg class="flag" viewBox="0 0 30 20"><rect width="10" height="20" fill="var(--flag-blue)"/><rect x="10" width="10" height="20" fill="var(--flag-white)"/><rect x="20" width="10" height="20" fill="var(--flag-red)"/><rect x=".5" y=".5" width="29" height="19" fill="none" stroke="var(--flag-edge)"/></svg><h2 class="node-name">Henri Valmont<br>(1916-2008) Students:</h2></header>
    <ul class="student-list is-long">
      <li>Jean-Luc Marchand (1947)<svg class="flag" viewBox="0 0 30 20"><rect width="10" height="20" fill="var(--flag-blue)"/><rect x="10" width="10" height="20" fill="var(--flag-white)"/><rect x="20" width="10" height="20" fill="var(--flag-red)"/><rect x=".5" y=".5" width="29" height="19" fill="none" stroke="var(--flag-edge)"/></svg></li>
      <li>Jacques Dorval (1947)<svg class="flag" viewBox="0 0 30 20"><rect width="10" height="20" fill="var(--flag-blue)"/><rect x="10" width="10" height="20" fill="var(--flag-white)"/><rect x="20" width="10" height="20" fill="var(--flag-red)"/><rect x=".5" y=".5" width="29" height="19" fill="none" stroke="var(--flag-edge)"/></svg></li>
      <li>Jean-Paul Fontaine (1944)<svg class="flag" viewBox="0 0 30 20"><rect width="10" height="20" fill="var(--flag-blue)"/><rect x="10" width="10" height="20" fill="var(--flag-white)"/><rect x="20" width="10" height="20" fill="var(--flag-red)"/><rect x=".5" y=".5" width="29" height="19" fill="none" stroke="var(--flag-edge)"/></svg></li>
    </ul>
  </article>

  <!-- Single-name nodes -->
  <article class="tree-node is-single" style="left:179px;top:1101px;width:223px;height:66px">
    <svg class="flag" viewBox="0 0 30 20"><rect width="10" height="20" fill="var(--flag-blue)"/><rect x="10" width="10" height="20" fill="var(--flag-white)"/><rect x="20" width="10" height="20" fill="var(--flag-red)"/><rect x=".5" y=".5" width="29" height="19" fill="none" stroke="var(--flag-edge)"/></svg><h2 class="node-name">Henri Valmont<br>(1916-2008)</h2>
  </article>
  <article class="tree-node is-single" style="left:799px;top:1101px;width:223px;height:66px">
    <svg class="flag" viewBox="0 0 30 20"><rect width="10" height="20" fill="var(--flag-blue)"/><rect x="10" width="10" height="20" fill="var(--flag-white)"/><rect x="20" width="10" height="20" fill="var(--flag-red)"/><rect x=".5" y=".5" width="29" height="19" fill="none" stroke="var(--flag-edge)"/></svg><h2 class="node-name">Henri Valmont<br>(1916-2008)</h2>
  </article>
  <article class="tree-node is-single" style="left:472px;top:1281px;width:223px;height:66px">
    <svg class="flag" viewBox="0 0 30 20"><rect width="10" height="20" fill="var(--flag-blue)"/><rect x="10" width="10" height="20" fill="var(--flag-white)"/><rect x="20" width="10" height="20" fill="var(--flag-red)"/><rect x=".5" y=".5" width="29" height="19" fill="none" stroke="var(--flag-edge)"/></svg><h2 class="node-name">Henri Valmont<br>(1916-2008)</h2>
  </article>
  <article class="tree-node is-single" style="left:472px;top:1415px;width:223px;height:66px">
    <svg class="flag" viewBox="0 0 30 20"><rect width="10" height="20" fill="var(--flag-blue)"/><rect x="10" width="10" height="20" fill="var(--flag-white)"/><rect x="20" width="10" height="20" fill="var(--flag-red)"/><rect x=".5" y=".5" width="29" height="19" fill="none" stroke="var(--flag-edge)"/></svg><h2 class="node-name">Henri Valmont<br>(1916-2008)</h2>
  </article>
</main>
</body>
</html>
```